Jest Ventures Website - Corporate Comedy Show

I've created a company called "Jest Ventures". We put on corporate comedy shows for companies all over the country. I'd like to design a nice, sleek, professional website, similar to Rydex's: https://www.rydex-example.com. We like the one page layout.
Tagline: Your Team's Desk-Grin Ratio
I need the following sections:
1. first section would be scrolling images of the company logo and tagline, with 2 or 3 other scrolling images. Testimonials.
2. The next section below would be an about the company section. a small paragraph describing what we do.
4. The next section below would be for a promo video
5. The next section below would be for bios...my partner and I would have transparent head shots, side by side split-screen. When you hover over our headshots, a button for "bio" appears. When you click the "bio" button, an expanded bio appears.
6. Contact section. Newsletter subscription. A section where people enter their email and short message of what they're linking for that will link directly to our email addresses.
7. Additional content. Scrolling video gallery of our sketch videos. (a section that links to a page with videos and content)
Target Market(s)
Corporate Executives, Event Planners, Event Coordinators, Marketing and HR managers, Venue owners
Industry/Entity Type
It Company
Coding
Coded - Design and coding required
Number of Pages Required
1 page
Font styles to use
Other font styles liked:
- FunctionPro
Requirements
Must have
- -Please use the branded colors from the logo. Burgundy and Blue;
- -A contact section where people put in their email address, company they are from and a small memo to describe the event they're hosting, which will then get sent directly to our email accounts;
- -email accounts that are "marcus@thejestventures.com" and "dennis@thejestventures.com" that link to our gmail accounts
- -getting our domain linked and hosted and all setup (www.thejestventures.com- bought from DomainNook)
Nice to have
- Build in Wix because we are familiar with it and know how to update
Should not have
- basic, generic look. too much white space (but soon is good!)

```html
<!DOCTYPE html>
<html lang="en">
<head>
<meta charset="utf-8">
<title>Jest Ventures — Corporate Comedy Shows</title>
<link rel="stylesheet" href="https://fonts.googleapis.com/css2?family=Montserrat:wght@400;600;700;800&family=Oswald:wght@300;400&display=swap">
<style>
  :root {
    --black: #000000;
    --ink: #0b0b0b;
    --footer: #1a1a1a;
    --white: #ffffff;
    --muted: #cfcfcf;
    --burgundy: #b01e2a;
    --burgundy-soft: rgba(176, 30, 42, 0.88);
    --blue: #2c6c8f;
    --social-1: #2f5f8a;
    --social-2: #2a8bb0;
    --social-3: #7a3f8e;
  }
  * { box-sizing: border-box; margin: 0; padding: 0; }
  html, body {
    width: 1200px; height: 2222px; overflow: hidden;
    background: var(--black); color: var(--white);
    font-family: "Montserrat", Arial, sans-serif;
  }
  a { color: inherit; text-decoration: none; }
  .page { position: relative; width: 1200px; height: 2222px; }

  /* Header */
  .site-header { position: absolute; left: 0; top: 0; width: 1200px; height: 148px; background: rgba(11,11,11,0.92); z-index: 3; }
  .brand { position: absolute; left: 272px; top: 18px; display: flex; align-items: center; gap: 18px; }
  .brand-dot { width: 72px; height: 72px; border-radius: 50%; background: var(--burgundy); }
  .brand-name { font-weight: 700; font-size: 24px; letter-spacing: 0.3px; color: var(--white); text-transform: uppercase; }
  .social { position: absolute; display: flex; gap: 4px; }
  .social span { width: 30px; height: 30px; border-radius: 50%; display: block; border: 1px solid rgba(255,255,255,0.25); }
  .social .s1 { background: var(--social-1); }
  .social .s2 { background: var(--social-2); }
  .social .s3 { background: var(--social-3); }
  .header-social { left: 826px; top: 13px; }
  .header-rule { position: absolute; left: 0; top: 106px; width: 1200px; height: 3px; background: var(--white); }
  .main-nav { position: absolute; left: 272px; top: 121px; display: flex; gap: 16px; font-size: 11px; font-weight: 700; color: var(--white); }

  /* Hero */
  .hero { position: absolute; left: 0; top: 148px; width: 1200px; height: 695px; }
  .hero-photo {
    position: absolute; inset: 0;
    background:
      radial-gradient(ellipse 420px 320px at 580px 280px, rgba(240,80,50,0.9), rgba(190,40,40,0) 75%),
      linear-gradient(90deg, #3a1410 0%, #a8321f 25%, #d9542f 50%, #c86a3a 72%, #5a3020 100%);
  }
  .hero-shade { position: absolute; left: 0; bottom: 0; width: 1200px; height: 260px; background: linear-gradient(180deg, rgba(0,0,0,0), rgba(0,0,0,0.55)); }
  .hero-tagline {
    position: absolute; left: 372px; top: 30px; width: 460px; text-align: center;
    font-family: "Oswald", Arial, sans-serif; font-weight: 300; font-size: 96px; line-height: 112px;
    text-transform: uppercase; color: var(--white);
  }

  /* About */
  .about-band { position: absolute; left: 0; top: 722px; width: 1200px; height: 121px; background: rgba(0,0,0,0.45); }
  .section-title { position: absolute; left: 0; width: 1200px; text-align: center; font-weight: 700; text-transform: uppercase; color: var(--white); }
  .about-title { top: 734px; font-size: 20px; letter-spacing: 1.5px; }
  .about-rule { position: absolute; left: 333px; top: 767px; width: 547px; height: 2px; background: var(--white); }
  .about-copy { position: absolute; left: 272px; top: 789px; width: 662px; font-size: 9.4px; line-height: 12px; font-weight: 700; color: var(--white); }
  .about-copy p { margin-bottom: 13px; }

  /* Video */
  .watch-title { top: 1037px; font-size: 21px; letter-spacing: 4px; }
  .video-frame {
    position: absolute; left: 304px; top: 1081px; width: 592px; height: 349px;
    background: radial-gradient(ellipse 260px 200px at 290px 130px, #6a4a32, #2c2118 80%);
  }
  .video-frame svg { position: absolute; left: 246px; top: 125px; }

  /* Profiles */
  .profiles-stage {
    position: absolute; left: -40px; top: 1480px; width: 1280px; height: 430px;
    background: radial-gradient(ellipse 640px 215px at 640px 215px, #3c3c3c 0%, #262626 55%, rgba(0,0,0,0) 100%);
  }
  .profiles-title { top: 1505px; font-size: 21px; letter-spacing: 6px; }
  .profile-card { position: absolute; top: 1545px; width: 315px; height: 290px; background: var(--white); }
  .profile-card.marcus { left: 270px; }
  .profile-card.dennis { left: 609px; }
  .profile-photo { position: absolute; left: 14px; top: 15px; width: 287px; height: 240px; }
  .marcus .profile-photo { background: linear-gradient(180deg, #6d6d6d, #4a4a4a 60%, #3a3a3a); }
  .dennis .profile-photo { background: linear-gradient(180deg, #e8ecef 0%, #c7ced3 45%, #6c5a4a 75%, #8a6a50 100%); }
  .profile-name { position: absolute; left: 0; top: 262px; width: 315px; text-align: center; color: var(--black); font-weight: 800; font-size: 16px; letter-spacing: 7px; text-transform: uppercase; }
  .view-profile {
    position: absolute; left: 82px; top: 131px; width: 148px; height: 41px;
    border: 2px solid var(--white); background: rgba(0,0,0,0.35);
    display: flex; align-items: center; justify-content: center;
    font-size: 11px; font-weight: 600; letter-spacing: 2.5px; text-transform: uppercase; color: var(--white);
  }

  /* Footer */
  .site-footer { position: absolute; left: 0; top: 1950px; width: 1200px; height: 272px; background: var(--footer); }
  .footer-col { position: absolute; top: 45px; font-size: 9px; color: var(--white); }
  .footer-col h4 { font-size: 9px; font-weight: 600; text-transform: uppercase; margin-bottom: 15px; color: var(--white); }
  .footer-col ul { list-style: none; }
  .footer-col li { margin-bottom: 15px; font-size: 9px; color: var(--white); }
  .col-1 { left: 272px; } .col-2 { left: 431px; } .col-3 { left: 591px; } .col-4 { left: 743px; }
  .footer-social { position: relative; gap: 2px; margin-top: 8px; }
  .legal { position: absolute; top: 232px; font-size: 8px; color: var(--muted); }
  .legal.left { left: 272px; }
  .legal.right { right: 272px; }
</style>
</head>
<body>
<div class="page">

  <header class="site-header">
    <div class="brand">
      <span class="brand-dot"></span>
      <span class="brand-name">Jest Ventures</span>
    </div>
    <div class="social header-social"><span class="s1"></span><span class="s2"></span><span class="s3"></span></div>
    <div class="header-rule"></div>
    <nav class="main-nav">
      <a href="#home">Home</a><a href="#about">About Us</a><a href="#gallery">Gallery</a><a href="#testimonials">Testimonials</a><a href="#contact">Contact Us</a>
    </nav>
  </header>

  <section class="hero" id="home">
    <div class="hero-photo" role="img" aria-label="Photo of two comedians on stools with microphones in front of a red stage backdrop"></div>
    <div class="hero-shade"></div>
    <h1 class="hero-tagline">Your<br>Team's<br>Desk-Grin<br>Ratio</h1>
  </section>

  <div class="about-band"></div>
  <h2 class="section-title about-title" id="about">About Us - More Tagline Text Here</h2>
  <div class="about-rule"></div>
  <div class="about-copy">
    <p>This is just a placeholder text. It is to be replaced with words of your choice. &nbsp; This is just a placeholder text. Replace this with your own. This is just a place holder text be replaced with words of your choice. &nbsp; This is just a placeholder text. Replace this with your own. This is just a placeholder text. It is to be replaced with words of your choice. &nbsp; This is just a placeholder text. Replace this with your own. This is just a placeholder text. It is to be replaced with words of your choice. &nbsp; This is just a placeholder text. Replace this with your own. This is just a placeholder text. It is to be replaced with words of your choice. &nbsp; This is just a placeholder text. Replace this with your own.</p>
    <p>This is just a placeholder text. It is to be replaced with words of your choice. &nbsp; This is just a placeholder text. Replace this with your own. This is just a place holder text be replaced with words of your choice. &nbsp; This is just a placeholder text. Replace this with your own. This is just a placeholder text. It is to be replaced with words of your choice. &nbsp; This is just a placeholder text. Replace this with your own. This is just a placeholder text. It is to be replaced with words of your choice. &nbsp; This is just a placeholder text. Replace this with your own. This is just a placeholder text. It is to be replaced with words of your choice. &nbsp; This is just a placeholder text. Replace this with your own.</p>
    <p>This is just a placeholder text. It is to be replaced with words of your choice. &nbsp; This is just a placeholder text. Replace this with your own. This is just a place holder text be replaced with words of your choice. &nbsp; This is just a placeholder text. Replace this with your own. This is just a placeholder text. Replace this with</p>
  </div>

  <h2 class="section-title watch-title">Watch Us In Action</h2>
  <div class="video-frame" role="img" aria-label="Video still of a comedian performing on a small stage in front of an audience">
    <svg width="100" height="100" viewBox="0 0 100 100" aria-hidden="true">
      <circle cx="50" cy="50" r="48" fill="var(--burgundy-soft)"/>
      <path d="M38 30 L72 50 L38 70 Z" fill="#d8d8d8"/>
    </svg>
  </div>

  <div class="profiles-stage"></div>
  <h2 class="section-title profiles-title">Profiles</h2>
  <article class="profile-card marcus">
    <div class="profile-photo" role="img" aria-label="Portrait of Marcus seated at a conference table"></div>
    <div class="view-profile">View Profile</div>
    <h3 class="profile-name">Marcus</h3>
  </article>
  <article class="profile-card dennis">
    <div class="profile-photo" role="img" aria-label="Portrait of Dennis leaning back in an office with feet on the table"></div>
    <h3 class="profile-name">Dennis</h3>
  </article>

  <footer class="site-footer">
    <div class="footer-col col-1"><h4>Footer Header Links Here</h4><ul><li>Footer links text here</li><li>Footer links text here</li><li>Footer links text here</li></ul></div>
    <div class="footer-col col-2"><h4>Footer Header Links Here</h4><ul><li>Footer links text here</li><li>Footer links text here</li><li>Footer links text here</li></ul></div>
    <div class="footer-col col-3"><h4>Footer Header Links Here</h4><ul><li>Footer links text here</li><li>Footer links text here</li><li>Footer links text here</li></ul></div>
    <div class="footer-col col-4"><h4>Follow Us</h4>
      <div class="social footer-social"><span class="s1"></span><span class="s2"></span><span class="s3"></span></div>
    </div>
    <p class="legal left">Terms &amp; Conditions | Site Map | Privacy</p>
    <p class="legal right">© Copyright text here 2015</p>
  </footer>

</div>
</body>
</html>
```